Quorvix Letter head

Quorvix is a young and energetic software development consultancy. We spend our time working with clients to turn what ever is in their heads in to software.
We are trying to create an image of a high class software boutique who build class leading bespoke solutions.
We need a sharp letter head that looks great on high quality media.
We like bold colours and distinctive design. So show us what you can do.
Industry/Entity Type
Software
Requirements
Must have
- Our company is based in the UK and are requried to have on the paper somewhere the following information:
* Registered company name: Quorvix Ltd
* Registered company number
* VAT registration number
In addition we also want the following:
* An email address
* Telephone number
* Website address
An example of what some pages have in their footer is something like the following:
Quorvix Ltd is registered in England and Wales. Reg. no: 5316274
Registered office: 48 Cobblewick Road, Harlow Essex, CM93TP. Tel: 07712365081
You do not have to use this sentance but please make sure your design incorporates accommodates the requirements for UK based companies

```html
<!DOCTYPE html>
<html lang="en">
<head>
<meta charset="utf-8">
<title>Quorvix Letterhead</title>
<link href="https://fonts.googleapis.com/css2?family=Open+Sans:wght@400;600&display=swap" rel="stylesheet">
<style>
  :root {
    --paper: #fafafa;
    --red-deep: #a8141f;
    --red-bright: #d41f2b;
    --mark-faint: #f4e7e9;
    --ink: #3a3a3a;
    --ink-soft: #555555;
  }
  html, body {
    margin: 0;
    padding: 0;
    overflow: hidden;
    background: var(--paper);
  }
  .letterhead {
    position: relative;
    width: 848px;
    height: 1200px;
    background: var(--paper);
    overflow: hidden;
    font-family: "Open Sans", Arial, sans-serif;
  }
  .edge-band,
  .faint-mark {
    position: absolute;
    left: 0;
    top: 0;
    width: 848px;
    height: 1200px;
  }
  .faint-mark text {
    font-family: "Open Sans", Arial, sans-serif;
    font-weight: 600;
    font-size: 150px;
    fill: var(--mark-faint);
  }
  .footer-block {
    position: absolute;
    left: 658px;
    top: 1060px;
    width: 182px;
    color: var(--ink);
  }
  .brand-name {
    font-size: 27px;
    font-weight: 600;
    color: var(--red-bright);
    letter-spacing: 1px;
    line-height: 1;
    margin: 0 0 9px;
  }
  .contact-list {
    font-size: 6.4px;
    line-height: 10.4px;
    color: var(--ink-soft);
  }
  .contact-row {
    display: flex;
  }
  .contact-label {
    width: 39px;
    flex: none;
  }
  .phone-group {
    display: flex;
  }
  .phone-col {
    width: 50px;
  }
  .mobile-label {
    width: 26px;
  }
  .registration {
    margin: 4px 0 0;
    font-size: 6.4px;
    line-height: 10.4px;
    color: var(--ink-soft);
  }
</style>
</head>
<body>
<main class="letterhead">
  <svg class="edge-band" viewBox="0 0 848 1200" aria-hidden="true">
    <defs>
      <linearGradient id="band-fill" x1="0" y1="0" x2="1" y2="0">
        <stop offset="0" style="stop-color: #a8141f"/>
        <stop offset="1" style="stop-color: #d41f2b"/>
      </linearGradient>
    </defs>
    <path d="M0 0 H274 C165 110, 45 290, 0 462 Z" fill="url(#band-fill)"/>
    <path d="M0 738 C45 910, 160 1085, 274 1200 H0 Z" fill="url(#band-fill)"/>
  </svg>

  <svg class="faint-mark" viewBox="0 0 848 1200" aria-hidden="true">
    <text x="120" y="636" textLength="624" lengthAdjust="spacingAndGlyphs">QUORVIX</text>
  </svg>

  <footer class="footer-block">
    <p class="brand-name">QUORVIX</p>
    <div class="contact-list">
      <div class="contact-row"><span class="contact-label">Address -</span><span>48 Cobblewick Road, Harlow Essex, CM93TP</span></div>
      <div class="contact-row"><span class="contact-label">Website -</span><span>www.quorvix-example.co.uk</span></div>
      <div class="contact-row"><span class="contact-label">E-mail -</span><span>hello@quorvix-example.co.uk</span></div>
      <div class="contact-row">
        <span class="contact-label">Telephone -</span>
        <div class="phone-group">
          <div class="phone-col">01279-480315<br>01279-480316<br>01279-480317</div>
          <span class="mobile-label">Mobile -</span>
          <div>07712365081<br>07712365082</div>
        </div>
      </div>
    </div>
    <p class="registration">Quorvix Ltd, registered in England and Wales<br>Company No. 5316274 &middot; VAT No. GB 284 7731 56</p>
  </footer>
</main>
</body>
</html>
```